Virtual Assistant/Online Marketing Business Card/Stationary

I need a professional but modern business card/stationary for my company in Dallas called BrivoLane. BrivoLane is a virtual assistant specializing in online marketing. I would like a unique design that stands out and makes my brand clear. Incorporating the logo is a must and have attached it to this brief.

Target Market(s)

small business owners & entrepreneurs, 35-65

Industry/Entity Type

Business

Contact Information for Business Card

Dorla Finch
dorlafinch@brivolane.biz
(214) 555-0187
brivolane.biz

Font styles to use
Sans Serif

Colors
f04a50
3176b5
9bcb3c

Requirements
Must have
• Colors that match the logo colors. Logo integration

```html
<!DOCTYPE html>
<html lang="en">
<head>
<meta charset="utf-8">
<title>BrivoLane Business Card</title>
<link rel="stylesheet" href="https://fonts.googleapis.com/css2?family=Ubuntu:wght@700&family=Roboto:ital,wght@0,400;1,400&display=swap">
<style>
  :root {
    --backdrop: #a9a6a7;
    --card: #fdfdfd;
    --ink: #33393e;
    --ink-soft: #3f454a;
    --brand-red: #f04a50;
    --brand-blue: #3176b5;
    --brand-green: #9bcb3c;
    --icon-teal: #3aa7b0;
  }
  * { margin: 0; padding: 0; box-sizing: border-box; }
  html, body {
    width: 1200px; height: 1200px; overflow: hidden;
    background: var(--backdrop);
  }
  .canvas { position: relative; width: 1200px; height: 1200px; }
  .card {
    position: absolute;
    width: 713px; height: 418px;
    background: var(--card);
    overflow: hidden;
  }
  .card--front { left: 238px; top: 119px; }
  .card--back { left: 230px; top: 644px; }
  .card__band {
    position: absolute; left: 0; bottom: 0;
    width: 100%; height: 6px;
    display: flex;
  }
  .card__band-part { flex: 1; }
  .card__band-part--green { background: var(--brand-green); flex: 1; }
  .card__band-part--blue { background: var(--brand-blue); flex: 3; }
  .card__band-part--red { background: var(--brand-red); flex: 1; }
  .wordmark {
    position: absolute;
    display: flex; align-items: center; gap: 14px;
    font-family: "Ubuntu", sans-serif; font-weight: 700;
    color: var(--ink); letter-spacing: -1px; white-space: nowrap;
  }
  .wordmark__dot { border-radius: 50%; background: var(--brand-red); flex: none; }
  .card--front .wordmark {
    left: 50%; top: 200px; transform: translate(-50%, -50%);
    font-size: 76px;
  }
  .card--front .wordmark__dot { width: 26px; height: 26px; }
  .card--back .wordmark {
    left: 195px; top: 200px; transform: translate(-50%, -50%);
    font-size: 50px; gap: 10px;
  }
  .card--back .wordmark__dot { width: 18px; height: 18px; }
  .contact {
    position: absolute; left: 395px; top: 128px;
    color: var(--ink-soft);
  }
  .contact__name {
    font-family: "Ubuntu", sans-serif; font-weight: 700;
    font-size: 29px; color: var(--ink); line-height: 1;
  }
  .contact__title {
    font-family: "Roboto", sans-serif; font-style: italic;
    font-size: 15px; margin-top: 9px;
  }
  .contact__list { list-style: none; margin-top: 30px; }
  .contact__item {
    display: flex; align-items: center; gap: 17px;
    font-family: "Roboto", sans-serif; font-size: 18px;
    height: 25.5px;
  }
  .contact__icon { width: 19px; height: 15px; flex: none; }
</style>
</head>
<body>
<div class="canvas">

  <section class="card card--front">
    <div class="wordmark"><span class="wordmark__dot"></span>BrivoLane</div>
    <div class="card__band" aria-hidden="true">
      <span class="card__band-part card__band-part--green"></span>
      <span class="card__band-part card__band-part--blue"></span>
      <span class="card__band-part card__band-part--red"></span>
    </div>
  </section>

  <section class="card card--back">
    <div class="wordmark"><span class="wordmark__dot"></span>BrivoLane</div>
    <div class="contact">
      <h1 class="contact__name">Dorla Finch</h1>
      <p class="contact__title">Managing Director</p>
      <ul class="contact__list">
        <li class="contact__item">
          <svg class="contact__icon" viewBox="0 0 19 15" aria-hidden="true">
            <path d="M1 5 Q9.5 -1 18 5 L15 7 L13 5 Q9.5 3.5 6 5 L4 7 Z" fill="var(--brand-green)"/>
            <rect x="4" y="7" width="11" height="7" rx="1" fill="var(--brand-green)"/>
            <circle cx="9.5" cy="10.5" r="2" fill="#fff"/>
          </svg>
          (214) 555-0187
        </li>
        <li class="contact__item">
          <svg class="contact__icon" viewBox="0 0 19 15" aria-hidden="true">
            <circle cx="9.5" cy="7.5" r="6.5" fill="var(--brand-red)"/>
            <g stroke="#fff" stroke-width="0.9" fill="none">
              <ellipse cx="9.5" cy="7.5" rx="2.8" ry="6.5"/>
              <line x1="3" y1="7.5" x2="16" y2="7.5"/>
              <line x1="4" y1="4.5" x2="15" y2="4.5"/>
              <line x1="4" y1="10.5" x2="15" y2="10.5"/>
            </g>
          </svg>
          www.brivolane.biz
        </li>
        <li class="contact__item">
          <svg class="contact__icon" viewBox="0 0 19 15" aria-hidden="true">
            <rect x="1.5" y="2" width="16" height="11" fill="var(--icon-teal)"/>
            <path d="M1.5 2 L9.5 9 L17.5 2 M1.5 13 L7.5 7.5 M17.5 13 L11.5 7.5" stroke="#fff" stroke-width="1" fill="none"/>
          </svg>
          dorlafinch@brivolane.biz
        </li>
      </ul>
    </div>
    <div class="card__band" aria-hidden="true">
      <span class="card__band-part card__band-part--green"></span>
      <span class="card__band-part card__band-part--blue"></span>
      <span class="card__band-part card__band-part--red"></span>
    </div>
  </section>

</div>
</body>
</html>
```